Pizza Box 10" x 10" - color: White

Custom design, utilizing CrustLoomo Logo and include the following information on the Pizza Box:

1. Custom Crafted Pizza with Quality Ingredients.
2. [....Get Your GAME ON] to be placed on the front flap and seen when the
box is opened.
3. You"ll miss 100% of the Pizza you don't eat.

4. Visit www.fennelcartonworks.example for additional design resource information. Go to site and then click on ORDERING to access.

5. The 10" x 10" Pizza Box is to be in the color WHITE.
6. Use colors Black and Red. no generic images. no food pics. I am looking for a clean and cool design.

Target Market(s)

Age 16 - 36 years

Industry/Entity Type

American Restaurant

Font styles to use
Sans Serif

Colors
ec1f27
000000
ffffff

Requirements
Must have
• Color Red and Black.
• Logo on Top and all sides of the Pizza Box.
Nice to have
• A Creative design that does not look generic.
Should not have
• No food images.

```html
<!DOCTYPE html>
<html lang="en">
<head>
<meta charset="utf-8">
<title>CrustLoomo Pizza Box</title>
<link rel="stylesheet" href="https://fonts.googleapis.com/css2?family=Archivo+Black&display=swap">
<style>
  :root {
    --red: #ec1f27;
    --black: #1f1f1f;
    --white: #ffffff;
    --backdrop: #e6e4e1;
    --art-tone: #ecebe9;
  }
  * { margin: 0; padding: 0; box-sizing: border-box; }
  html, body {
    width: 1200px; height: 960px; overflow: hidden;
    background: var(--backdrop);
    font-family: "Archivo Black", "Arial Black", sans-serif;
  }
  .box {
    position: absolute; left: 250px; top: 30px;
    width: 700px; height: 900px;
  }
  .lid {
    position: relative; width: 700px; height: 740px;
    background: var(--white);
  }
  .brand {
    position: absolute; left: 14px; top: 150px;
    transform-origin: left top; transform: rotate(-90deg);
    display: flex; align-items: center; gap: 7px;
    color: var(--black); font-size: 18px; letter-spacing: 0.5px;
  }
  .brand-dot {
    width: 18px; height: 18px; border-radius: 50%;
    border: 2px solid var(--red);
  }
  .slice-art {
    position: absolute; left: 50px; top: 130px;
    width: 270px; height: 500px;
    background: var(--art-tone);
    border-radius: 250px 0 0 250px;
  }
  .slogan {
    position: absolute; left: 330px; top: 120px; width: 340px;
    text-transform: uppercase; line-height: 0.95;
  }
  .slogan span { display: block; color: var(--black); }
  .slogan .accent { color: var(--red); }
  .s-youll { font-size: 56px; }
  .s-miss { font-size: 88px; }
  .s-pct { font-size: 80px; }
  .s-ofthe { font-size: 54px; }
  .s-pizza { font-size: 100px; letter-spacing: -3px; }
  .s-dont { font-size: 46px; }
  .s-eat { font-size: 124px; }
  .flap {
    width: 700px; height: 120px; background: var(--white);
    border-top: 2px solid #d8d6d3;
    display: flex; align-items: center; padding: 0 20px;
  }
  .flap-band {
    width: 100%; height: 64px; background: var(--red);
    display: flex; align-items: center; justify-content: center;
    color: var(--white); font-size: 24px; letter-spacing: 1px;
    text-transform: uppercase;
  }
</style>
</head>
<body>
  <div class="box">
    <div class="lid">
      <div class="brand"><span class="brand-dot"></span><span>CrustLoomo</span></div>
      <div class="slice-art" role="img" aria-label="Line drawing of a pizza cut into four slices with toppings"></div>
      <h1 class="slogan">
        <span class="s-youll">You’ll</span>
        <span class="s-miss">Miss</span>
        <span class="s-pct accent">100%</span>
        <span class="s-ofthe">Of the</span>
        <span class="s-pizza accent">Pizza</span>
        <span class="s-dont">You don’t</span>
        <span class="s-eat accent">Eat</span>
      </h1>
    </div>
    <div class="flap">
      <div class="flap-band">[...Get your game on]</div>
    </div>
  </div>
</body>
</html>
```